Building Certification Company needs a professional letterhead and report template

We are a modern company within an ageing industry. Our industry is responsible for life safety aspects of the built environment, we ensure buildings are safe and fit for occupation.

We use letterhead and reports everyday, we need a smart and professional letterhead that reflects the serious nature of the work we do. We also require a report template of the same ilk.

Target Market(s)

Our target market will consist mainly of professional architects, developers and construction companies.

Industry/Entity Type

Industry

Requirements
Must have
• The letterhead must have:-
Our logo
Our company details, including address, website, email, phone

Address - Suite 208 / 45 Harwick Lane Dunmore NSW 2100

Website - www.quillstonecompliance.example.au

Email - info@qsc.example.au

Phone - 02 5550 3846

The report template must have:-
A title page, which is to incorporate our logo or an aspect of our logo, get creative people.

```html
<!DOCTYPE html>
<html lang="en">
<head>
<meta charset="utf-8">
<title>Quillstone Compliance Letterhead</title>
<link href="https://fonts.googleapis.com/css2?family=Montserrat:wght@500;600&display=swap" rel="stylesheet">
<style>
  :root {
    --paper: #ffffff;
    --brand: #3f5f86;
    --brand-light: #6f8fb3;
    --ink: #2b2f36;
    --band-light: #a9b5c4;
    --band-dark: #4e6580;
  }
  html, body {
    margin: 0;
    padding: 0;
    overflow: hidden;
    background: var(--paper);
  }
  .letterhead {
    position: relative;
    width: 900px;
    height: 1200px;
    background: var(--paper);
    font-family: "Montserrat", sans-serif;
    overflow: hidden;
  }
  .brand {
    position: absolute;
    top: 14px;
    left: 0;
    width: 100%;
    display: flex;
    flex-direction: column;
    align-items: center;
    gap: 10px;
  }
  .brand-mark {
    width: 48px;
    height: 48px;
    background: var(--brand-light);
  }
  .brand-name {
    font-weight: 600;
    font-size: 15px;
    letter-spacing: 3px;
    color: var(--brand);
    text-transform: uppercase;
  }
  .contact {
    position: absolute;
    top: 1108px;
    left: 0;
    width: 100%;
    text-align: center;
    font-style: normal;
    font-weight: 500;
    font-size: 8.5px;
    line-height: 11px;
    color: var(--ink);
  }
  .contact p { margin: 0; }
  .footer-band {
    position: absolute;
    left: 0;
    bottom: 0;
    width: 100%;
    height: 32px;
    display: flex;
  }
  .footer-band .band-left {
    flex: 0 0 460px;
    background: var(--band-light);
  }
  .footer-band .band-right {
    flex: 1;
    background: var(--band-dark);
  }
</style>
</head>
<body>
  <main class="letterhead">
    <header class="brand">
      <div class="brand-mark" aria-hidden="true"></div>
      <div class="brand-name">Quillstone Compliance</div>
    </header>

    <footer>
      <address class="contact">
        <p>Suite 208 / 45 Harwick Lane Dunmore NSW 2100</p>
        <p>www.quillstonecompliance.example.au</p>
        <p>Email: info@qsc.example.au</p>
        <p>Phone: 02 5550 3846</p>
      </address>
      <div class="footer-band">
        <div class="band-left" role="img" aria-label="Decorative striped band in grey-blue tones"></div>
        <div class="band-right" aria-hidden="true"></div>
      </div>
    </footer>
  </main>
</body>
</html>
```